Tallow Electrical Business Card

We need a business card design for our family-run electrical contracting business based in Western Australia called 'Tallow Electrical'. We provide electrical services including residential, commercial and industrial. We aim for individual business cards to be made for all of our employees. We already have a company logo, which we require to be featured on the design. We would like simple, sleek and vibrant designs, which incorporate our logo and represent our business. We do not want anything involving too many graphics/images. We like the colours red, black, white and all shades of grey. The final design should communicate professionalism and trustworthiness.
We require the following contact information:
Name- Peter Hargreave
EC 5810
Mobile number- 0455 902 318
Fax number (including area code)- (08) 9576 2083
Email adress- name@tallowelectric.com.au
Industry/Entity Type
Electrical
Font styles to use
Other font styles liked:
- ITC Handel Bold
Look and feel

```html
<!DOCTYPE html>
<html lang="en">
<head>
<meta charset="utf-8">
<title>Tallow Electrical Business Card</title>
<link href="https://fonts.googleapis.com/css2?family=Open+Sans:wght@400;700&family=Michroma&display=swap" rel="stylesheet">
<style>
  :root {
    --backdrop: #1e1e1e;
    --card: #ffffff;
    --card-shade: #ececec;
    --ink: #2b2b2b;
    --ink-soft: #3c3c3c;
    --rule: #b9b9b9;
    --brand-red: #d3232e;
    --faint-red: rgba(211, 35, 46, 0.13);
  }
  * { box-sizing: border-box; margin: 0; padding: 0; }
  html, body { width: 1200px; height: 871px; overflow: hidden; }
  body {
    background: var(--backdrop);
    font-family: "Open Sans", Arial, sans-serif;
    color: var(--ink);
    display: flex;
    flex-direction: column;
    align-items: center;
    justify-content: center;
    gap: 56px;
  }
  .card {
    position: relative;
    width: 630px;
    height: 360px;
    background: linear-gradient(135deg, var(--card) 0%, var(--card) 55%, var(--card-shade) 100%);
    overflow: hidden;
    box-shadow: 0 14px 30px rgba(0,0,0,0.45);
  }
  .brand {
    display: flex;
    align-items: center;
    gap: 10px;
    font-weight: 700;
    color: var(--ink);
    text-transform: uppercase;
    letter-spacing: 0.04em;
    line-height: 1;
    white-space: nowrap;
  }
  .brand-mark { width: 22px; height: 22px; background: var(--brand-red); flex: none; }
  .card-back .brand {
    position: absolute;
    left: 50%; top: 50%;
    transform: translate(-50%, -50%);
    font-size: 32px;
  }
  .card-back .brand-mark { width: 30px; height: 30px; }
  .card-front .brand {
    position: absolute;
    left: 70px; top: 52px;
    font-size: 26px;
  }
  .watermark {
    position: absolute;
    right: -40px; top: 70px;
    width: 260px; height: 260px;
    background: var(--faint-red);
  }
  .divider {
    position: absolute;
    left: 0; right: 0; top: 145px;
    height: 1px;
    background: var(--rule);
  }
  .licence {
    position: absolute;
    left: 110px; top: 160px;
    font-size: 14px;
    color: var(--ink-soft);
  }
  .contacts {
    position: absolute;
    left: 70px; top: 196px;
    list-style: none;
    display: flex;
    flex-direction: column;
    gap: 10px;
    font-size: 16px;
    color: var(--ink-soft);
  }
  .contacts li { display: flex; align-items: center; gap: 22px; white-space: nowrap; }
  .contacts svg { width: 16px; height: 16px; flex: none; }
  .holder {
    position: absolute;
    right: 40px; top: 200px;
    font-family: "Michroma", "Open Sans", sans-serif;
    font-size: 15px;
    letter-spacing: 0.2em;
    text-transform: uppercase;
    white-space: nowrap;
    color: var(--ink);
    padding-bottom: 6px;
    border-bottom: 1px solid var(--rule);
  }
</style>
</head>
<body>
  <section class="card card-back">
    <div class="brand"><span class="brand-mark"></span>Tallow Electrical</div>
  </section>

  <section class="card card-front">
    <div class="watermark"></div>
    <div class="brand"><span class="brand-mark"></span>Tallow Electrical</div>
    <div class="divider"></div>
    <p class="licence">EC 5810</p>
    <ul class="contacts">
      <li>
        <svg viewBox="0 0 16 16" aria-hidden="true"><rect x="4" y="1" width="8" height="14" rx="1.5" fill="none" stroke="#d3232e" stroke-width="1.4"/><line x1="7" y1="12.5" x2="9" y2="12.5" stroke="#d3232e" stroke-width="1.4"/></svg>
        <span>0455 902 318</span>
      </li>
      <li>
        <svg viewBox="0 0 16 16" aria-hidden="true"><rect x="4" y="1.5" width="8" height="4" fill="none" stroke="#d3232e" stroke-width="1.3"/><rect x="1.5" y="5.5" width="13" height="6" rx="1" fill="none" stroke="#d3232e" stroke-width="1.3"/><rect x="4" y="9.5" width="8" height="5" fill="#fff" stroke="#d3232e" stroke-width="1.3"/></svg>
        <span>(08) 9576 2083</span>
      </li>
      <li>
        <svg viewBox="0 0 16 16" aria-hidden="true"><rect x="1.5" y="3.5" width="13" height="9" fill="none" stroke="#d3232e" stroke-width="1.4"/><polyline points="1.5,3.5 8,9 14.5,3.5" fill="none" stroke="#d3232e" stroke-width="1.4"/></svg>
        <span>name@tallowelectric.com.au</span>
      </li>
    </ul>
    <p class="holder">Peter Hargreave</p>
  </section>
</body>
</html>
```